Website for Apartment Rental in Prague

I would like to create designs of my website focused on luxury apartment rentals in Prague, Czech Republic. I created initial mock-ups, They are all attached. I need to design homepage and subpage. The mock-ups were created by combining elements from different websites that I liked but I need you to create a design that is unique and original. The attached files a only a guidance for the structure of the website but not for the design. Try to be creative.

Industry/Entity Type

Apartment

```html
<!DOCTYPE html>
<html lang="en">
<head>
<meta charset="utf-8">
<title>Casa Lumen Apartments Prague</title>
<link rel="stylesheet" href="https://fonts.googleapis.com/css2?family=Montserrat:wght@400;500;600;700&family=Open+Sans:ital,wght@0,400;0,600;0,700;1,700&display=swap">
<style>
:root{
  --brown:#a37f63;
  --brown-dark:#8d6c53;
  --accent:#f0561c;
  --ink:#222;
  --muted:#666;
  --grey:#ececec;
  --light:#f6f6f6;
  --footer:#2a2a2a;
  --footer-deep:#1f1f1f;
  --white:#fff;
}
*{box-sizing:border-box;margin:0;padding:0}
html,body{width:1200px;height:5042px;overflow:hidden}
body{font-family:"Open Sans",Arial,sans-serif;color:var(--ink);background:var(--white);font-size:13px}
.heading{font-family:"Montserrat",Arial,sans-serif;font-weight:500;font-size:30px;text-align:center;color:var(--ink)}

/* top bar */
.topbar{height:34px;display:flex;align-items:center;justify-content:space-between;padding:0 60px;font-size:11px;color:#555;border-bottom:1px solid #eee}
.topbar .group{display:flex;gap:34px;align-items:center}
.topbar .dot{display:inline-block;width:10px;height:10px;background:var(--brown);border-radius:50%;margin-right:6px;vertical-align:middle}
.social-mini{display:flex;gap:8px}
.social-mini span{width:10px;height:10px;background:#888;border-radius:50%}

/* nav */
.nav{height:94px;display:flex;align-items:center;justify-content:space-between;padding:0 40px 0 60px}
.logo{font-family:"Montserrat",Arial,sans-serif;font-weight:600;color:var(--brown-dark);font-size:15px;line-height:1.2;letter-spacing:1px}
.logo small{display:block;font-size:10px;letter-spacing:3px}
.menu{display:flex;gap:22px;font-family:"Montserrat",Arial,sans-serif;font-weight:600;font-size:12px;color:var(--brown-dark)}

/* hero */
.hero{height:562px;position:relative;background:linear-gradient(100deg,#d9d6d1 0%,#efece7 40%,#cfc8bd 70%,#5b4a3d 100%)}
.hero-title{position:absolute;left:259px;top:190px;font-family:"Montserrat",Arial,sans-serif;font-weight:700;font-size:50px;color:var(--white);letter-spacing:1px}
.booking{position:absolute;left:218px;top:408px;width:808px;height:104px;background:rgba(255,255,255,.72);padding:14px 20px;display:grid;grid-template-columns:repeat(5,1fr);gap:6px 14px;font-size:11px}
.booking label{display:block;color:#444;margin-bottom:3px}
.booking .field{height:24px;background:var(--white);border:1px solid #ccc;padding:4px 6px;font-size:11px}
.booking .wide{grid-column:span 2}
.booking .btn{background:var(--brown);color:var(--white);height:24px;display:flex;align-items:center;justify-content:center;font-size:11px;align-self:end}
.booking .or{align-self:end;display:flex;gap:8px;align-items:center}

/* card sections */
.listing{position:relative;text-align:center}
.listing .heading{padding-top:70px}
.cards{display:flex;gap:44px;justify-content:center;margin-top:46px;text-align:left}
.card{width:282px}
.card h3{font-family:"Montserrat",Arial,sans-serif;font-size:13px;font-weight:600;color:var(--brown-dark);line-height:1.35;height:38px}
.card .photo{height:200px;margin-top:6px;position:relative}
.card .price{position:absolute;right:0;bottom:12px;background:var(--accent);color:var(--white);font-size:12px;font-weight:600;padding:6px 14px}
.card .meta{display:flex;justify-content:space-between;font-size:11px;color:var(--accent);margin-top:8px}
.card p{font-size:11px;color:var(--muted);line-height:1.4;margin-top:5px}
.card .actions{display:flex;gap:24px;margin-top:12px}
.card .actions span{width:128px;height:34px;background:var(--brown);color:var(--white);display:flex;align-items:center;justify-content:center;font-size:12px}
.arrow{position:absolute;top:50%;width:20px;height:40px}
.arrow.left{left:58px}.arrow.right{right:68px}
.just-booked{height:547px;background:var(--white)}
.popular{height:582px;background:var(--brown)}
.popular .heading{color:var(--white)}
.popular .card{background:var(--white);padding:10px 0 10px}
.popular .card h3,.popular .card .meta,.popular .card p{padding:0 8px}
.popular .card .actions{padding:0 8px}
.popular .card .actions span{background:var(--accent)}
.best-price{height:628px;background:var(--white)}

.p1{background:linear-gradient(135deg,#e9e4dc,#c9b59a 55%,#7a5f47)}
.p2{background:linear-gradient(135deg,#f1efe9,#cfc9bf 60%,#8a8278)}
.p3{background:linear-gradient(135deg,#3a2b22,#8a5a38 55%,#d9a36a)}

/* need to know */
.need{height:511px;background:var(--grey);text-align:center}
.need .heading{padding-top:150px}
.facts{display:flex;justify-content:center;gap:120px;margin-top:74px}
.fact{width:190px}
.fact h4{font-family:"Montserrat",Arial,sans-serif;font-size:19px;font-weight:500}
.fact p{font-size:11px;color:#555;margin-top:10px;line-height:1.4}
.btn-accent{display:inline-block;background:var(--accent);color:var(--white);font-family:"Montserrat",Arial,sans-serif;font-weight:600;font-size:11px;letter-spacing:.5px;padding:10px 22px}
.need .btn-accent{margin-top:48px}

/* partner */
.partner{height:554px;background:linear-gradient(180deg,#2c2c2c 0%,#4a4a4a 50%,#333 100%);text-align:center;position:relative}
.partner h2{padding-top:165px;font-family:"Montserrat",Arial,sans-serif;font-weight:500;font-size:62px;color:var(--white);letter-spacing:1px}
.partner .sub{font-family:"Open Sans",Arial,sans-serif;font-style:italic;font-weight:700;font-size:34px;color:var(--accent);margin-top:4px}
.partner .btn-accent{margin-top:44px}

/* testimonials */
.testimonials{height:471px;background:var(--brown);text-align:center}
.testimonials .heading{color:var(--white);padding-top:56px}
.quotes{display:flex;justify-content:center;gap:28px;margin-top:56px;text-align:left}
.quote{width:325px;position:relative;padding-top:40px}
.quote .who{position:absolute;left:18px;top:0;display:flex;gap:12px;align-items:flex-start}
.avatar{width:62px;height:62px;border-radius:50%;background:linear-gradient(135deg,#ddd,#aaa);border:3px solid var(--white)}
.who b{display:block;color:var(--white);font-size:11px;margin-top:10px}
.who small{color:#f0e6dd;font-size:10px}
.quote p{background:var(--white);padding:36px 20px 18px;font-size:12px;line-height:1.5;color:#444;height:168px}
.dots{display:flex;justify-content:center;gap:10px;margin-top:46px}
.dots span{width:11px;height:11px;border-radius:50%;background:#d8c8ba}
.dots span:first-child{background:var(--white)}

/* gallery */
.gallery{height:732px;background:var(--white);text-align:center}
.gallery .heading{padding-top:84px}
.gallery .intro{width:1000px;margin:18px auto 0;font-size:11px;color:#444;line-height:1.5}
.grid{display:grid;grid-template-columns:repeat(5,1fr);gap:4px;width:1010px;margin:18px auto 0;height:470px}
.grid div:nth-child(3n+1){background:linear-gradient(135deg,#efeae3,#b8a28a)}
.grid div:nth-child(3n+2){background:linear-gradient(135deg,#6f8a8c,#d5d9d4)}
.grid div:nth-child(3n){background:linear-gradient(135deg,#8a6a4e,#e8ddd0)}

/* footer */
.footer{height:276px;background:var(--footer);color:#ccc;display:flex;padding:24px 80px 0;gap:50px;font-size:11px}
.footer h5{font-family:"Montserrat",Arial,sans-serif;color:var(--white);font-size:13px;font-weight:600;margin-bottom:16px}
.links{display:grid;grid-template-columns:170px 150px;gap:0}
.links ul{list-style:none;line-height:1.8}
.links li::before{content:"› ";color:var(--accent)}
.contact ul{list-style:none;line-height:2}
.map{width:260px;height:170px;background:linear-gradient(135deg,#e7e3da,#c8d3d8)}
.follow .icons{display:flex;gap:10px}
.follow .icons span{width:16px;height:16px;background:#bbb;border-radius:50%}
.follow .call{margin-top:70px;color:var(--white);font-family:"Montserrat",Arial,sans-serif;font-weight:600;font-size:12px}
.follow .call b{display:block;font-size:22px}
.copyright{height:51px;background:var(--footer-deep);color:#999;font-size:11px;display:flex;align-items:center;justify-content:center}
</style>
</head>
<body>

<div class="topbar">
  <div class="group"><span>OUR HOSPITALITY</span><span>EN ⌄</span><span>DISCOVER PRAGUE ⌄</span></div>
  <div class="group"><span><i class="dot"></i>1-555-0148-220</span><span><i class="dot"></i>hello@casalumen.example</span><div class="social-mini"><span></span><span></span><span></span><span></span></div></div>
</div>

<header class="nav">
  <div class="logo">Casa Lumen<small>APARTMENTS PRAGUE</small></div>
  <nav class="menu"><span>APARTMENTS</span><span>LOCATION</span><span>SERVICES</span><span>GALLERY</span><span>NEWS</span><span>EXCLUSIVE OFFERS &amp; TOURS</span><span>FOR FAMILIES</span><span>CONTACT US</span></nav>
</header>

<section class="hero" role="img" aria-label="Bright apartment living room with white brick wall, plant and fireplace">
  <h1 class="hero-title">BEING HOME IN PRAGUE</h1>
  <form class="booking">
    <div><label>Check in date</label><div class="field">20/11/2017</div></div>
    <div><label>Check out date</label><div class="field">27/11/2017</div></div>
    <div><label>Adults</label><div class="field">4 ⌄</div></div>
    <div><label>Children</label><div class="field">2 ⌄</div></div>
    <div><label>Infants</label><div class="field">0 ⌄</div></div>
    <div class="wide"><label>Promotional code</label><div class="field"></div></div>
    <div class="btn">Check Availability</div>
    <div class="or wide"><span>Or</span><div class="field" style="flex:1">Select Rental Unit ⌄</div></div>
  </form>
</section>

<section class="listing just-booked">
  <h2 class="heading">Just Booked</h2>
  <svg class="arrow left" viewBox="0 0 20 40"><path d="M16 2 4 20l12 18" fill="none" stroke="#999" stroke-width="2"/></svg>
  <svg class="arrow right" viewBox="0 0 20 40"><path d="M4 2l12 18L4 38" fill="none" stroke="#999" stroke-width="2"/></svg>
  <div class="cards">
    <article class="card"><h3>Brand New Luxury Living Stunning Contemporary Design</h3><div class="photo p1" role="img" aria-label="Living room with colourful sofa"><span class="price">From 150 USD</span></div><div class="meta"><span>1 bedroom</span><span>4 Max People</span></div><p>Lorem ipsum dolor sit amet, consectetur adipiscing elit. In eu enim pretium est id, quod dictum esse expeditum...</p><div class="actions"><span>Details</span><span>Book now</span></div></article>
    <article class="card"><h3>Brand New Zen Luxury Living Apartment in the Center of Prague</h3><div class="photo p2" role="img" aria-label="White minimalist apartment interior"><span class="price">From 200 USD</span></div><div class="meta"><span>1 bedroom</span><span>4 Max People</span></div><p>Lorem ipsum dolor sit amet, consectetur adipiscing elit. In eu enim pretium est id, quod dictum esse expeditum...</p><div class="actions"><span>Details</span><span>Book now</span></div></article>
    <article class="card"><h3>Expedition Prague! Top Locate Brand New Apartment</h3><div class="photo p3" role="img" aria-label="Warmly lit bedroom"><span class="price">From 225 USD</span></div><div class="meta"><span>1 bedroom</span><span>4 Max People</span></div><p>Lorem ipsum dolor sit amet, consectetur adipiscing elit. In eu enim pretium est id, quod dictum esse expeditum...</p><div class="actions"><span>Details</span><span>Book now</span></div></article>
  </div>
</section>

<section class="need">
  <h2 class="heading">Need to Know</h2>
  <div class="facts">
    <div class="fact"><h4>Apartments</h4><p>also available to rent all the apartments together for companies or larger groups</p></div>
    <div class="fact"><h4>Check-Out</h4><p>until noon; earlier check-in, 3pm - both are flexible, by arrangement</p></div>
    <div class="fact"><h4>Rates</h4><p>Prices from 150 USD per night, including tax</p></div>
  </div>
  <span class="btn-accent">PLEASE LEAVE A MESSAGE</span>
</section>

<section class="listing popular">
  <h2 class="heading">Popular</h2>
  <svg class="arrow left" viewBox="0 0 20 40"><path d="M16 2 4 20l12 18" fill="none" stroke="#e6d8cc" stroke-width="2"/></svg>
  <svg class="arrow right" viewBox="0 0 20 40"><path d="M4 2l12 18L4 38" fill="none" stroke="#e6d8cc" stroke-width="2"/></svg>
  <div class="cards">
    <article class="card"><h3>Brand New Sunny Penthouse with a view of Prague</h3><div class="photo p1" role="img" aria-label="Sunny penthouse living area"><span class="price">From 250 USD</span></div><div class="meta"><span>Studio</span><span>4 Max People</span></div><p>Lorem ipsum dolor sit amet, consectetur adipiscing elit. In eu enim pretium est id, quod dictum esse expeditum...</p><div class="actions"><span>Details</span><span>Book now</span></div></article>
    <article class="card"><h3>Brand New Modern Apartment Unbeatable Location</h3><div class="photo p2" role="img" aria-label="Modern open kitchen and lounge"><span class="price">From 275 USD</span></div><div class="meta"><span>1 bedroom</span><span>4 Max People</span></div><p>Lorem ipsum dolor sit amet, consectetur adipiscing elit. In eu enim pretium est id, quod dictum esse expeditum...</p><div class="actions"><span>Details</span><span>Book now</span></div></article>
    <article class="card"><h3>Brand New Luxury Living Stunning Contemporary Design</h3><div class="photo p3" role="img" aria-label="Dark luxury lounge at night"><span class="price">From 300 USD</span></div><div class="meta"><span>1 bedroom</span><span>4 Max People</span></div><p>Lorem ipsum dolor sit amet, consectetur adipiscing elit. In eu enim pretium est id, quod dictum esse expeditum...</p><div class="actions"><span>Details</span><span>Book now</span></div></article>
  </div>
</section>

<section class="listing best-price">
  <h2 class="heading">Best Price</h2>
  <svg class="arrow left" viewBox="0 0 20 40"><path d="M16 2 4 20l12 18" fill="none" stroke="#999" stroke-width="2"/></svg>
  <svg class="arrow right" viewBox="0 0 20 40"><path d="M4 2l12 18L4 38" fill="none" stroke="#999" stroke-width="2"/></svg>
  <div class="cards">
    <article class="card"><h3>Brand New Sunny Penthouse with a view of Prague</h3><div class="photo p1" role="img" aria-label="Sunny penthouse living area"><span class="price">From 250 USD</span></div><div class="meta"><span>Studio</span><span>4 Max People</span></div><p>Lorem ipsum dolor sit amet, consectetur adipiscing elit. In eu enim pretium est id, quod dictum esse expeditum...</p><div class="actions"><span>Details</span><span>Book now</span></div></article>
    <article class="card"><h3>Brand New Modern Apartment Unbeatable Location</h3><div class="photo p2" role="img" aria-label="Modern open kitchen and lounge"><span class="price">From 275 USD</span></div><div class="meta"><span>1 bedroom</span><span>4 Max People</span></div><p>Lorem ipsum dolor sit amet, consectetur adipiscing elit. In eu enim pretium est id, quod dictum esse expeditum...</p><div class="actions"><span>Details</span><span>Book now</span></div></article>
    <article class="card"><h3>Brand New Luxury Living Stunning Contemporary Design</h3><div class="photo p3" role="img" aria-label="Dark luxury lounge at night"><span class="price">From 250 USD</span></div><div class="meta"><span>1 bedroom</span><span>4 Max People</span></div><p>Lorem ipsum dolor sit amet, consectetur adipiscing elit. In eu enim pretium est id, quod dictum esse expeditum...</p><div class="actions"><span>Details</span><span>Book now</span></div></article>
  </div>
</section>

<section class="partner" role="img" aria-label="Dark photo of a business handshake">
  <h2>PARTNER WITH US</h2>
  <p class="sub">Earn money rent your property</p>
  <span class="btn-accent">MESSAGE US</span>
</section>

<section class="testimonials">
  <h2 class="heading">Testimonials</h2>
  <div class="quotes">
    <div class="quote"><div class="who"><div class="avatar" role="img" aria-label="Guest portrait"></div><div><b>TOMAS REYNER</b><small>Guest</small></div></div><p>Lorem ipsum dolor sit amet, consectetur adipiscing elit. Quod autem habent admirationis, cum prope accesseris? An hoc usque quaque, aliter in vita?</p></div>
    <div class="quote"><div class="who"><div class="avatar" role="img" aria-label="Guest portrait"></div><div><b>MS ELSA KOLAR</b><small>Traveller</small></div></div><p>Quid ergo, sed audiebamus modo de Carneade? Bene autem corpore hoc sunt, quod potest esse justum, tertium. Quis ille ergo totum quod praeter Pyrrhonem.</p></div>
    <div class="quote"><div class="who"><div class="avatar" role="img" aria-label="Guest portrait"></div><div><b>MR IVO BERMAN</b><small>Business guest</small></div></div><p>Ita ut sit, inquit, negare! Itaque hic ipse iam pridem est reiectus; finem enim iam habes, quod vel tamen ceteros, Quam vis neque simul ipsum primo dici.</p></div>
  </div>
  <div class="dots"><span></span><span></span><span></span><span></span><span></span></div>
</section>

<section class="gallery">
  <h2 class="heading">Gallery</h2>
  <p class="intro">Lorem ipsum dolor sit amet, consectetur adipiscing elit. At ego quem huic anteponam non audeo dicere; sed ea mala virtuti magnitudine obruebantur. Duo Reges: constructio interrete. Quam nihil sit lenius, quam cum rationem tenemus et quieti sumus, qui Epicurus in hoc loco sentiunt. Negat enim summo bono afferre incrementum diem, quod omnes sapientes summum bonum putarent et omnia semper ad voluptatem rettulerunt.</p>
  <div class="grid" role="img" aria-label="Ten photos of apartment interiors, bedrooms, kitchens and terraces">
    <div></div><div></div><div></div><div></div><div></div><div></div><div></div><div></div><div></div><div></div>
  </div>
</section>

<footer class="footer">
  <div class="links-col"><h5>Quick Links</h5>
    <div class="links">
      <ul><li>Apartments</li><li>Location</li><li>Services</li><li>Gallery</li><li>News</li><li>Exclusive offers &amp; Tours</li><li>For Families</li><li>Contact us</li></ul>
      <ul><li>About us</li><li>Careers</li><li>Press</li><li>Policies</li><li>Help</li><li>Business Travel</li><li>Partner with us</li></ul>
    </div>
  </div>
  <div class="contact"><h5>Contact us</h5><ul><li>48 Ember Lane, Northfield, 20418</li><li>☎ 1-555-0148-220</li><li>☎ 1-555-0148-221</li><li>✉ hello@casalumen.example</li><li>⌂ www.casalumen.example</li></ul></div>
  <div><h5>FIND US</h5><div class="map" role="img" aria-label="Street map showing the apartment location"></div></div>
  <div class="follow"><h5>FOLLOW US ON</h5><div class="icons"><span></span><span></span><span></span><span></span></div><div class="call">CALL US ON<b>1-555-0148-220</b></div></div>
</footer>
<div class="copyright">© 2017 casalumen | Privacy Policy | User Agreement</div>

</body>
</html>
```